Hi, Looking for an upgraded business card to the aged one attached. Open to suggestions and no real limitations, but if your going to use a picture of a taxi i think it should be vector based rather than a full color picture. I've uploaded a 2 pictures of the type of taxi which is a Velmora K7 in white. The taxi markings look like the pink one in the picture but to be clear his is white. The taxi is in Bermuda so if you wanted to include something island based that's ok as well but not required. The other thing he wanted to keep on there was the bermuda police crest, with the retired police office incorporated somehow.

Requirements
Must have
• Bermuda Taxi Operator
Retired Police Officer
Police Crest
Taxi #
Email
Mobile Number

```html
<!DOCTYPE html>
<html lang="en">
<head>
<meta charset="utf-8">
<title>Bermuda Taxi Operator – Business Card</title>
<link href="https://fonts.googleapis.com/css2?family=Fredoka:wght@600&family=Open+Sans:wght@400;700&display=swap" rel="stylesheet">
<style>
  :root {
    --page-bg: #d9d2c7;
    --card-bg: #ece5d9;
    --card-edge: #f6f1e9;
    --navy: #1f4868;
    --ink: #3a3733;
    --van-light: #e4e0d8;
    --van-dark: #8f8a82;
  }
  * { box-sizing: border-box; margin: 0; padding: 0; }
  html, body {
    width: 1200px;
    height: 1047px;
    overflow: hidden;
    background: var(--page-bg);
  }
  .card {
    position: absolute;
    left: 151px;
    top: 291px;
    width: 947px;
    height: 516px;
    background: var(--card-bg);
    border: 2px solid var(--card-edge);
    border-radius: 22px;
    font-family: "Open Sans", Arial, sans-serif;
    color: var(--ink);
  }
  .agency-mark {
    position: absolute;
    left: 50px;
    top: 58px;
    width: 170px;
    display: flex;
    flex-direction: column;
    align-items: center;
    gap: 12px;
  }
  .agency-mark .dot {
    width: 80px;
    height: 80px;
    border-radius: 50%;
    background: var(--navy);
  }
  .agency-mark .agency-name {
    font-weight: 700;
    font-size: 20px;
    line-height: 1.2;
    color: var(--navy);
    text-align: center;
  }
  .headline {
    position: absolute;
    left: 520px;
    top: 36px;
    width: 406px;
    font-family: "Fredoka", "Arial Rounded MT Bold", sans-serif;
    font-weight: 600;
    font-size: 63px;
    line-height: 69px;
    letter-spacing: 3px;
    color: var(--navy);
    text-align: center;
    text-transform: uppercase;
  }
  .owner {
    position: absolute;
    left: 50px;
    top: 251px;
  }
  .owner .name {
    font-weight: 700;
    font-size: 38px;
    color: var(--navy);
    line-height: 46px;
  }
  .owner .role {
    font-size: 25px;
    line-height: 35px;
  }
  .contact p {
    position: absolute;
    font-size: 24px;
    line-height: 1;
    white-space: nowrap;
  }
  .contact .taxi-no { left: 46px; top: 367px; }
  .contact .line {
    left: 45px;
    display: flex;
    align-items: center;
    gap: 22px;
  }
  .contact .phone { top: 405px; }
  .contact .email { top: 440px; }
  .contact svg { width: 26px; height: 26px; fill: var(--navy); flex: none; }
  .taxi-visual {
    position: absolute;
    left: 486px;
    top: 297px;
    width: 362px;
    height: 156px;
    border-radius: 40px 60px 18px 18px;
    background: linear-gradient(180deg, var(--van-light) 0%, #cfcac1 60%, var(--van-dark) 100%);
  }
</style>
</head>
<body>
  <div class="card">
    <div class="agency-mark">
      <span class="dot"></span>
      <span class="agency-name">Coral Isle Police</span>
    </div>

    <h1 class="headline">Bermuda<br>Taxi<br>Operator</h1>

    <div class="owner">
      <p class="name">Rowan Ellery</p>
      <p class="role">Retired Police Officer</p>
    </div>

    <div class="contact">
      <p class="taxi-no">Taxi # T2718</p>
      <p class="line phone">
        <svg viewBox="0 0 24 24" aria-hidden="true"><path d="M6.6 10.8a15.1 15.1 0 0 0 6.6 6.6l2.2-2.2a1 1 0 0 1 1-.25 11.4 11.4 0 0 0 3.6.57 1 1 0 0 1 1 1V20a1 1 0 0 1-1 1A17 17 0 0 1 3 4a1 1 0 0 1 1-1h3.5a1 1 0 0 1 1 1c0 1.25.2 2.45.57 3.57a1 1 0 0 1-.25 1z"/></svg>
        <span>1-441-555-0147</span>
      </p>
      <p class="line email">
        <svg viewBox="0 0 24 24" aria-hidden="true"><path d="M2 5h20v1.2L12 13.5 2 6.2z"/><path d="M2 8l10 7.3L22 8v11H2z"/></svg>
        <span>rellery208@coralmail.com</span>
      </p>
    </div>

    <div class="taxi-visual" role="img" aria-label="White Velmora K7 passenger van, side view"></div>
  </div>
</body>
</html>
```